Cedarloft Supply METAL business card

A metal business card design. Attached are older designs for a reference, but we want a NEW design, not the same as in the past. See the 2 examples just posted. We would like some cut out in the design. Possibly the pine cone or the pine tree branch (see image IMG_0).

Target Market(s)

Home and Gardern

Industry/Entity Type

Landscape

Contact Information for Business Card

Logo, website, address, name, phone numbers

```html
<!DOCTYPE html>
<html lang="en">
<head>
<meta charset="utf-8">
<title>Cedarloft Supply Business Card</title>
<link rel="stylesheet" href="https://fonts.googleapis.com/css2?family=Montserrat:wght@400;600;700&display=swap">
<style>
  :root {
    --backdrop: #3a3a3a;
    --card-black: #0e0e0e;
    --emboss: #222222;
    --card-white: #ffffff;
    --rust: #c0541f;
    --navy: #2b2f7a;
    --ink: #222222;
    --flag-blue: #3a3f9e;
    --flag-red: #d3262e;
  }
  * { box-sizing: border-box; margin: 0; padding: 0; }
  html, body {
    width: 1200px; height: 689px; overflow: hidden;
    background: var(--backdrop);
    font-family: "Montserrat", sans-serif;
  }
  .stage {
    position: relative; width: 1200px; height: 689px;
    display: flex; align-items: center; justify-content: center; gap: 40px;
  }
  .card {
    position: relative; width: 540px; height: 309px;
    border-radius: 22px; overflow: hidden;
  }
  .card--front { background: var(--card-black); }
  .card--back { background: var(--card-white); }

  .front-name {
    position: absolute; inset: 0;
    display: flex; align-items: center; justify-content: center;
    font-weight: 700; font-size: 44px; color: var(--emboss);
    letter-spacing: 0.5px;
  }

  .back-brand {
    position: absolute; left: 34px; top: 40px;
    font-weight: 700; font-size: 30px; line-height: 1.05; color: var(--rust);
  }
  .holder {
    position: absolute; left: 34px; top: 132px;
    font-weight: 700; font-size: 20px; color: var(--rust);
  }
  .address {
    position: absolute; left: 34px; top: 168px;
    font-size: 12.5px; line-height: 1.35; color: var(--ink);
  }
  .contacts {
    position: absolute; left: 34px; top: 212px;
    list-style: none; font-size: 12.5px; color: var(--ink);
  }
  .contacts li { display: flex; align-items: center; gap: 9px; height: 21px; }
  .contacts svg { width: 12px; height: 12px; fill: var(--rust); flex: none; }

  .flag-art {
    position: absolute; right: 0; top: 40px; width: 210px; height: 230px;
    background: linear-gradient(160deg, var(--flag-blue) 0%, var(--flag-blue) 42%, var(--flag-red) 58%, #e65a5f 100%);
    border-radius: 40px 0 0 80px;
    opacity: 0.92;
  }
</style>
</head>
<body>
  <main class="stage">
    <section class="card card--front" aria-label="Card front">
      <div class="front-name">Cedarloft Supply</div>
    </section>

    <section class="card card--back" aria-label="Card back">
      <div class="back-brand">Cedarloft<br>Supply</div>
      <div class="flag-art" role="img" aria-label="Brushed American flag illustration with a pine cone"></div>
      <h1 class="holder">Dalton Mercer</h1>
      <p class="address">48 Birchgate Lane<br>Fairhaven, MS 39000</p>
      <ul class="contacts">
        <li>
          <svg viewBox="0 0 12 12"><path d="M1 4c0-2 2-3 5-3s5 1 5 3l-2 1-1-1.5H4L3 5 1 4zm2 2h6l1 5H2l1-5zm3 1a1.5 1.5 0 100 3 1.5 1.5 0 000-3z"/></svg>
          888.555.0142
        </li>
        <li>
          <svg viewBox="0 0 12 12"><path d="M3 0h6a1 1 0 011 1v10a1 1 0 01-1 1H3a1 1 0 01-1-1V1a1 1 0 011-1zm0 2v7h6V2H3zm3 8a.7.7 0 100 1.4A.7.7 0 006 10z"/></svg>
          601.555.0187
        </li>
        <li>
          <svg viewBox="0 0 12 12"><path d="M6 0a6 6 0 110 12A6 6 0 016 0zm0 1.2a4.8 4.8 0 00-4.7 3.8h9.4A4.8 4.8 0 006 1.2zM1.3 7a4.8 4.8 0 009.4 0H1.3z"/></svg>
          www.cedarloftsupply.com
        </li>
      </ul>
    </section>
  </main>
</body>
</html>
```